Stationery and Business Card Design

We need stationary design for our new company pelvanta. Pelvanta is a company that provides city apartment rentals for tourists in Athens We need business cards, letterheads for A4 and A5 and envelopes for A4 A5. The design needs to be modern, friendly and corporate.

Target Market(s)

City Tourists

Industry/Entity Type

Tourism

```html
<!DOCTYPE html>
<html lang="en">
<head>
<meta charset="utf-8">
<title>Pelvanta Letterhead</title>
<link href="https://fonts.googleapis.com/css2?family=Raleway:wght@400&display=swap" rel="stylesheet">
<style>
  :root {
    --backdrop: #ffffff;
    --paper: #f2f2f4;
    --brand: #8b0050;
    --brand-pale: #e9dde3;
  }
  html, body {
    margin: 0;
    padding: 0;
    width: 1200px;
    height: 900px;
    overflow: hidden;
    background: var(--backdrop);
  }
  .canvas {
    position: relative;
    width: 1200px;
    height: 900px;
  }
  .letterhead {
    position: absolute;
    left: 342px;
    top: 162px;
    width: 490px;
    height: 660px;
    background: var(--paper);
    overflow: hidden;
  }
  .header-rule {
    position: absolute;
    left: 0;
    top: 97px;
    width: 312px;
    height: 3px;
    background: var(--brand);
  }
  .brand-block {
    position: absolute;
    right: 2px;
    top: 40px;
    width: 118px;
    display: flex;
    flex-direction: column;
    align-items: center;
  }
  .brand-square {
    width: 33px;
    height: 33px;
    background: var(--brand);
  }
  .brand-name {
    margin-top: 5px;
    font-family: "Raleway", sans-serif;
    font-weight: 400;
    font-size: 29px;
    line-height: 1;
    letter-spacing: -0.3px;
    color: var(--brand);
    white-space: nowrap;
  }
  .backdrop-square {
    position: absolute;
    left: 87px;
    top: 208px;
    width: 330px;
    height: 330px;
    background: var(--brand-pale);
  }
  .footer-swoosh {
    position: absolute;
    left: 0;
    top: 0;
    width: 490px;
    height: 660px;
  }
</style>
</head>
<body>
<div class="canvas">
  <div class="letterhead">
    <div class="header-rule"></div>
    <div class="brand-block">
      <div class="brand-square"></div>
      <div class="brand-name">Pelvanta</div>
    </div>
    <div class="backdrop-square"></div>
    <svg class="footer-swoosh" viewBox="0 0 490 660" aria-hidden="true">
      <path d="M0,656 C205,648 450,615 490,528 L490,660 L0,660 Z" fill="var(--brand)"/>
    </svg>
  </div>
</div>
</body>
</html>
```